Poster - Series of Poster Designs

We have a number of motivational quotes related to weight loss and fitness which need putting into a series of posters.
The designs need to:
- Reflect the current brand (see www.bluefernhaven.com.au)
- Be designed with scalability in mind to fit to A1, A3, A4, and A5. All portrait layout.
- Incorporate our logo
- Any images need to relfect the diversity of our clients ranging from 70kgs up to 200kgs.
- We have a stock of photos which can be used, or you can source your own (subject to budget approval)
Total of 26 posters in total, but all on the same design series (so effectively 1 design, with 26 applications).
The series of quotes are attached. An example quote would be:
-
"The difference between your body this week and next week is what you do for the next seven days to achieve your goals"
-
Our clients are a range of ages (20 - 60) and split male/female so colours should be neutral and reflect our orange/green branding. A modern feel but not super modern.
Output needs to be A3 ready to print with all source files included so that we can amend in the future.
There may be ongoing work for the right designer.

```html
<!DOCTYPE html>
<html lang="en">
<head>
<meta charset="utf-8">
<title>Bluefern Haven – Believe Poster</title>
<link rel="stylesheet" href="https://fonts.googleapis.com/css2?family=Righteous&display=swap">
<style>
  :root {
    --photo-warm: #f0b040;
    --photo-orange: #e7883a;
    --photo-floor: #3a2c2a;
    --type-white: #ffffff;
    --type-shadow: rgba(90, 50, 20, 0.75);
    --type-outline: #6b4420;
  }
  html, body {
    margin: 0;
    padding: 0;
    overflow: hidden;
    background: #ffffff;
  }
  .poster {
    position: relative;
    width: 850px;
    height: 1200px;
    overflow: hidden;
    font-family: "Righteous", "Arial Rounded MT Bold", sans-serif;
  }
  .poster__photo {
    position: absolute;
    inset: 0;
    background:
      radial-gradient(ellipse 300px 380px at 660px 620px, rgba(217, 112, 138, 0.85), rgba(217, 112, 138, 0) 100%),
      radial-gradient(ellipse 260px 200px at 560px 120px, rgba(226, 110, 60, 0.9), rgba(226, 110, 60, 0) 100%),
      linear-gradient(180deg, var(--photo-warm) 0%, var(--photo-orange) 70%, #b8683a 92%, var(--photo-floor) 100%);
  }
  .quote {
    position: absolute;
    left: 32px;
    top: 108px;
    margin: 0;
    color: var(--type-white);
    font-size: 72px;
    font-weight: 400;
    line-height: 87px;
    letter-spacing: 4px;
    text-shadow: 3px 4px 4px var(--type-shadow);
  }
  .quote__line {
    display: block;
    white-space: nowrap;
  }
  .quote__line--boxed {
    display: flex;
    gap: 8px;
    height: 87px;
    align-items: center;
  }
  .quote__box {
    display: inline-block;
    background: var(--type-white);
    padding: 0 4px 0 6px;
    height: 60px;
    line-height: 66px;
    font-size: 76px;
    letter-spacing: 3px;
    color: var(--type-white);
    -webkit-text-stroke: 2px var(--type-outline);
    text-shadow: 3px 3px 0 var(--type-outline);
    box-shadow: 0 0 0 3px var(--type-outline) inset;
  }
  .brand {
    position: absolute;
    right: 34px;
    bottom: 44px;
    margin: 0;
    color: var(--type-white);
    font-size: 38px;
    letter-spacing: 2px;
    line-height: 1;
  }
</style>
</head>
<body>
  <main class="poster">
    <div class="poster__photo" role="img" aria-label="Photo of a smiling woman in a pink vest and grey pants standing with a hand on her hip in a gym, exercise balls behind her"></div>

    <h1 class="quote">
      <span class="quote__line">a HUGE PART</span>
      <span class="quote__line">OF LOSING</span>
      <span class="quote__line">WEIGHT IS</span>
      <span class="quote__line quote__line--boxed"><span class="quote__box">BELIEVING</span></span>
      <span class="quote__line quote__line--boxed"><span class="quote__box">THAT</span><span class="quote__box">YOU</span></span>
      <span class="quote__line quote__line--boxed"><span class="quote__box">CAN</span><span class="quote__box">DO</span><span class="quote__box">IT</span></span>
      <span class="quote__line">&amp; REALISING</span>
      <span class="quote__line">THAT IT’S</span>
      <span class="quote__line">NOT GOING</span>
      <span class="quote__line">TO HAPPEN</span>
      <span class="quote__line">OVERNIGHT</span>
    </h1>

    <p class="brand">Bluefern Haven</p>
  </main>
</body>
</html>
```